Lending Harbor Partners - business cards

we need new business cards for my company.
i've been in business for 25 years.
my wife and I are mortgage brokers.

we just bought the domain for a website with www.homekeyfunding.example
that could be used in the design also.

On the business card would be
Front card:

Dale Whitcomb
Owner/Loan Officer
Cell: (555) 314-2297
Lending Harbor Partners
4172 Pinecrest Lane
Cedar Hollow, CA 93512
Office (555) 490-6631
Fax (555) 490-6674
website www.homekeyfunding.example

Back of Card:

LHP BRE #0378215 NMLS #586249
Dale Whitcomb BRE # 04519863 NMLS #587716

Industry/Entity Type

Business

```html
<!DOCTYPE html>
<html lang="en">
<head>
<meta charset="utf-8">
<title>Lending Harbor Partners – Business Card</title>
<link rel="stylesheet" href="https://fonts.googleapis.com/css2?family=Questrial&display=swap">
<style>
  :root {
    --paper: #ffffff;
    --band: #fafafa;
    --rust: #a4522a;
    --ink: #4a4a4a;
    --ink-soft: #5a5a5a;
    --rule: #b5754f;
  }
  * { margin: 0; padding: 0; box-sizing: border-box; }
  html, body {
    width: 1200px; height: 686px; overflow: hidden;
    background: var(--paper);
  }
  .card {
    position: relative; width: 1200px; height: 686px;
    background: var(--paper);
    font-family: "Questrial", "Century Gothic", sans-serif;
    color: var(--ink);
  }
  .brand-band {
    position: absolute; left: 0; top: 166px; width: 566px; height: 209px;
    background: var(--band);
  }
  .brand-name {
    position: absolute; left: 0; width: 588px; top: 378px;
    text-align: center;
    font-size: 25px; letter-spacing: 1.5px; text-transform: uppercase;
    color: var(--rust);
  }
  .divider {
    position: absolute; left: 570px; top: 34px; width: 1px; height: 606px;
    background: linear-gradient(to bottom, rgba(181,117,79,0) 0%, var(--rule) 40%, var(--rule) 60%, rgba(181,117,79,0) 100%);
  }
  .person { position: absolute; left: 641px; top: 96px; }
  .person-name { font-size: 42px; font-weight: 400; color: var(--rust); line-height: 1.05; }
  .person-title { font-size: 27px; color: var(--ink-soft); margin-top: 4px; }
  .contact-group { position: absolute; left: 630px; display: flex; }
  .contact-icon { width: 36px; height: 34px; margin-right: 25px; flex: none; fill: var(--rust); }
  .contact-icon.icon-outline { fill: none; stroke: var(--rust); stroke-width: 1.8; }
  .contact-lines { font-size: 28.5px; line-height: 34.5px; }
  .group-address { top: 288px; }
  .group-phone { top: 425px; }
  .group-web { top: 562px; }
</style>
</head>
<body>
<div class="card">
  <div class="brand-band"></div>
  <div class="brand-name">Lending Harbor Partners</div>

  <div class="divider"></div>

  <div class="person">
    <h1 class="person-name">Dale Whitcomb</h1>
    <p class="person-title">Owner/Loan Officer</p>
  </div>

  <div class="contact-group group-address">
    <svg class="contact-icon" viewBox="0 0 36 34" aria-hidden="true">
      <path d="M18 3 L2 18 L6 18 L18 7 L30 18 L34 18 Z"/>
      <path d="M8 19 L18 10 L28 19 L28 32 L21 32 L21 24 L15 24 L15 32 L8 32 Z"/>
      <rect x="25" y="5" width="4" height="8"/>
    </svg>
    <div class="contact-lines">
      Lending Harbor Partners<br>
      4172 Pinecrest Lane<br>
      Cedar Hollow, CA 93512
    </div>
  </div>

  <div class="contact-group group-phone">
    <svg class="contact-icon" viewBox="0 0 36 34" aria-hidden="true">
      <path d="M3 11 C3 5 33 5 33 11 L33 14 L25 14 L25 10 L11 10 L11 14 L3 14 Z"/>
      <path d="M10 15 L13 12 L23 12 L26 15 L32 25 L32 29 L4 29 L4 25 Z"/>
      <circle cx="18" cy="21" r="3.5" fill="#ffffff"/>
    </svg>
    <div class="contact-lines">
      Cell: (555) 314-2297<br>
      Office: (555) 490-6631<br>
      Fax: (555) 490-6674
    </div>
  </div>

  <div class="contact-group group-web">
    <svg class="contact-icon icon-outline" viewBox="0 0 36 34" aria-hidden="true">
      <circle cx="18" cy="19" r="13"/>
      <ellipse cx="18" cy="19" rx="6" ry="13"/>
      <line x1="18" y1="6" x2="18" y2="32"/>
      <line x1="5" y1="19" x2="31" y2="19"/>
      <path d="M7 12 H29 M7 26 H29"/>
    </svg>
    <div class="contact-lines">www.homekeyfunding.example</div>
  </div>
</div>
</body>
</html>
```